High end business card design for custom homebuilding company

Looking for a high end business card design that is unique and elegant. Can use embossing, foil printing, laser die cutting, or any high end printing technique or high end paper. Will upload current design so you can see the logo and what we are using currently, but we want something more unique and elegant. I included our logo to help with design.

Target Market(s)

High end custom home buyers of $1.5 million plus homes. Also real estate developers of high end communities.

Industry/Entity Type

Business

Contact Information for Business Card

Double sided. We want something very elegant and expensive looking. We are looking to incorporate a combination of perhaps linen paper or a high end paper, with foil stamping or embossing/debossing to make the card look unique, but still elegant. We tend to use blacks and golds, but are open to any ideas. Looking for creative and unique design.

Colors

Designer to choose colors to be used in the design.

Requirements
Must have
• High end, elegant look. Can use foil, embossing, or high end papers like linen. We want to make the card unique and interesting, but elegant and expensive looking.
Nice to have
• I am including just some cards I saw that looked interesting for one reason or another. I like a clean elegant design and like both the clean white style, and the blacks. So not sure if we want a black design or white. Would like to see both.

```html
<!DOCTYPE html>
<html lang="en">
<head>
<meta charset="utf-8">
<title>Hollowmere Custom Homes – Business Card</title>
<link rel="stylesheet" href="https://fonts.googleapis.com/css2?family=Cinzel:wght@400;600&family=PT+Sans:wght@400&display=swap">
<style>
  :root {
    --backdrop: #d8b98f;
    --card-white: #fbfbfa;
    --card-black: #050505;
    --ink-grey: #5a5a58;
    --gold: #c8bd55;
    --white: #ffffff;
    --rule: #4a4a4a;
  }
  * { margin: 0; padding: 0; box-sizing: border-box; }
  html, body {
    width: 1200px; height: 1144px; overflow: hidden;
    background: var(--backdrop);
  }
  .canvas { position: relative; width: 1200px; height: 1144px; }

  .card { position: absolute; box-shadow: 0 3px 8px rgba(0,0,0,.35); }
  .card--front { left: 308px; top: 183px; width: 584px; height: 360px; background: var(--card-white); }
  .card--back  { left: 310px; top: 583px; width: 581px; height: 358px; background: var(--card-black); }

  .brand { position: absolute; font-family: "Cinzel", serif; font-weight: 600; text-align: right; line-height: 1; }
  .brand__name { display: block; letter-spacing: 1px; }
  .brand__sub { display: block; letter-spacing: 11px; margin-top: 4px; }

  .card--front .brand { left: 0; right: 0; top: 150px; text-align: center; color: var(--ink-grey); }
  .card--front .brand__name { font-size: 46px; }
  .card--front .brand__sub { font-size: 17px; letter-spacing: 12px; }

  .card--back .brand { right: 31px; top: 36px; color: var(--white); }
  .card--back .brand__name { font-size: 38px; }
  .card--back .brand__sub { font-size: 15px; }

  .person { position: absolute; left: 39px; top: 155px; }
  .person__name { font-family: "Cinzel", serif; font-weight: 600; font-size: 22px; color: var(--gold); letter-spacing: .5px; line-height: 1; }
  .person__role { font-family: "PT Sans", sans-serif; font-size: 15px; color: var(--white); margin-top: 4px; }
  .divider { position: absolute; left: 188px; right: 31px; top: 192px; height: 1px; background: var(--rule); }

  .contact { position: absolute; right: 30px; top: 205px; list-style: none; font-family: "PT Sans", sans-serif; font-size: 15.5px; color: var(--white); text-align: right; }
  .contact li { height: 21px; line-height: 21px; display: flex; justify-content: flex-end; align-items: center; gap: 4px; white-space: nowrap; }
  .contact svg { width: 12px; height: 12px; fill: var(--gold); flex: none; }
  .address { position: absolute; right: 30px; top: 296px; font-family: "PT Sans", sans-serif; font-size: 15.5px; line-height: 21px; color: var(--white); text-align: right; font-style: normal; white-space: nowrap; }
</style>
</head>
<body>
<main class="canvas">
  <section class="card card--front" aria-label="Card front">
    <div class="brand">
      <span class="brand__name">HOLLOWMERE</span>
      <span class="brand__sub">CUSTOM HOMES</span>
    </div>
  </section>

  <section class="card card--back" aria-label="Card back">
    <div class="brand">
      <span class="brand__name">HOLLOWMERE</span>
      <span class="brand__sub">CUSTOM HOMES</span>
    </div>

    <div class="person">
      <p class="person__name">Daniel Whitford</p>
      <p class="person__role">Managing Director</p>
    </div>
    <div class="divider"></div>

    <ul class="contact">
      <li>321 555 0174
        <svg viewBox="0 0 12 12" aria-hidden="true"><path d="M1 4c0-2 2-3 5-3s5 1 5 3l-2 1-1-1.5H4L3 5zM2.5 6h7l1 5h-9z"/></svg></li>
      <li>321 555 0188
        <svg viewBox="0 0 12 12" aria-hidden="true"><path d="M3 0h6v12H3zM4 1.5v8h4v-8z"/></svg></li>
      <li>hello@hollowmere.com
        <svg viewBox="0 0 12 12" aria-hidden="true"><path d="M0 2h12v8H0zM1 3l5 4 5-4z"/></svg></li>
      <li>www.hollowmere.com
        <svg viewBox="0 0 12 12" aria-hidden="true"><circle cx="6" cy="6" r="5.5"/></svg></li>
    </ul>
    <address class="address">418 Linden Ridge Road, Suite 2<br>Asheville, NC 28801</address>
  </section>
</main>
</body>
</html>
```